Business Card Design

We have recently seen two business cards that caught our attention and think the designs would work for us. We are an accounting firm that serves small businesses in a variety of industries. Attached are the two business card that inspired us along with very rough layouts. We would like to see a professional layout using our company information.

Industry/Entity Type

Accounting

Contact Information for Business Card

Company Name - Dalworth Pryce
Address - 4180 Brambleton Lane, Suite 310, Houston, TX 77051
713-508-9627 - Main
281-369-0714 - Fax

Team Member Names, emails and phone numbers (see attachment)

```html
<!DOCTYPE html>
<html lang="en">
<head>
<meta charset="utf-8">
<title>Dalworth Pryce – Business Cards</title>
<link href="https://fonts.googleapis.com/css2?family=Open+Sans:wght@400;600;700&display=swap" rel="stylesheet">
<style>
  :root {
    --backdrop-top: #f4f4f4;
    --backdrop-bottom: #d9d9d9;
    --card: #ffffff;
    --card-edge: #e6e6e6;
    --charcoal: #363636;
    --slate: #8a8a8a;
    --ink: #2f2f2f;
    --paper-text: #ffffff;
  }
  * { box-sizing: border-box; margin: 0; padding: 0; }
  html, body { width: 1200px; height: 883px; overflow: hidden; }
  body {
    background: linear-gradient(180deg, var(--backdrop-top), var(--backdrop-bottom));
    font-family: "Open Sans", Arial, sans-serif;
    color: var(--ink);
    position: relative;
  }
  .card {
    position: absolute;
    width: 520px;
    height: 296px;
    background: var(--card);
    border: 1px solid var(--card-edge);
    border-radius: 26px;
    overflow: hidden;
    box-shadow: 0 14px 30px rgba(0,0,0,0.14);
  }
  .card--brand { left: 560px; top: 96px; }
  .card--contact { left: 120px; top: 470px; }

  /* Brand side */
  .brand {
    position: absolute;
    left: 46px; top: 142px;
    display: flex; align-items: center; gap: 12px;
  }
  .brand__square { width: 30px; height: 30px; background: var(--slate); }
  .brand__name { font-size: 25px; font-weight: 700; color: var(--ink); letter-spacing: 0.2px; }
  .web-tab {
    position: absolute; left: 290px; top: 40px;
    width: 162px; height: 72px;
    background: var(--charcoal);
    display: flex; align-items: center; justify-content: center;
    padding: 0 10px;
    white-space: nowrap;
    color: var(--paper-text);
    font-size: 7.5px; letter-spacing: 1.1px; text-transform: uppercase;
  }
  .web-tab__accent {
    position: absolute; left: 452px; top: 40px;
    width: 68px; height: 72px; background: var(--slate);
  }

  /* Contact side */
  .person {
    position: absolute; left: 0; top: 40px; width: 100%;
    text-align: center;
  }
  .person__name { font-size: 20px; font-weight: 400; letter-spacing: 0.5px; text-transform: uppercase; }
  .person__name b { font-weight: 700; }
  .person__title { font-size: 10.5px; text-transform: uppercase; letter-spacing: 0.3px; }
  .person__title b { font-weight: 700; }

  .band-dark {
    position: absolute; left: 262px; top: 98px;
    width: 258px; height: 92px;
    background: var(--charcoal); color: var(--paper-text);
    display: flex; flex-direction: column; justify-content: center; align-items: center;
    font-size: 11px; line-height: 1.45; text-transform: uppercase;
    white-space: nowrap;
  }
  .band-light {
    position: absolute; left: 0; top: 150px;
    width: 262px; height: 94px;
    background: var(--slate); color: var(--paper-text);
    display: flex; flex-direction: column; justify-content: center;
    padding-left: 78px;
    font-size: 12px; line-height: 1.35;
    white-space: nowrap;
  }
  .band-light__label { text-transform: uppercase; }
  .band-light__strip {
    position: absolute; left: 0; top: 150px;
    width: 18px; height: 94px; background: var(--charcoal);
  }
  .address {
    position: absolute; left: 0; top: 250px; width: 100%;
    text-align: center; font-size: 9.5px; line-height: 1.45;
    text-transform: uppercase;
  }
  .address b { font-weight: 700; }
</style>
</head>
<body>

  <section class="card card--brand" aria-label="Business card, brand side">
    <div class="brand">
      <span class="brand__square" aria-hidden="true"></span>
      <span class="brand__name">Dalworth Pryce</span>
    </div>
    <div class="web-tab">www.dalworthpryce.com</div>
    <div class="web-tab__accent" aria-hidden="true"></div>
  </section>

  <section class="card card--contact" aria-label="Business card, contact side">
    <div class="person">
      <p class="person__name">Marcus <b>Ellery</b></p>
      <p class="person__title"><b>Senior</b> Tax Accountant</p>
    </div>

    <div class="band-dark">
      <p>Email &amp; Web</p>
      <p>contact@dalworthpryce.com</p>
      <p>www.dalworthpryce.com</p>
    </div>

    <div class="band-light">
      <p class="band-light__label">Phone &amp; Fax</p>
      <p>713-508-9627</p>
      <p>281-369-0714</p>
    </div>
    <div class="band-light__strip" aria-hidden="true"></div>

    <div class="address">
      <p>4180 <b>Brambleton Lane</b>, Suite 310,</p>
      <p><b>Houston, TX 77051</b></p>
    </div>
  </section>

</body>
</html>
```